Business card design needed

I am a small start up business in the mortgage broking industry based in Sydney called 'nest2keys'. I will be providing residential mortgages to first home owners, investors and people looking to refinance. I would like to see designs that use the colors blue, black, and white - same as my logo (see logo design uploaded)

Target Market(s)

My target market is First Home Owners, property investors, and people looking to refinance. The loans I will be providing are for residential property only at this stage, and my clients will predominantly be in the 30-50yr age bracket.

Industry/Entity Type

Residential

Contact Information for Business Card

Owen Presley
Director/Mobile Mortgage Broker
nests2keys
PO BOX 2984
West Calder NSW 2175
Mb: 0471 286 904
email: owen@brickvaleplex.com.au

Requirements
Must have
• please use lower case for business name (i.e. nests2keys)

```html
<!DOCTYPE html>
<html lang="en">
<head>
<meta charset="utf-8">
<title>nests2keys business card</title>
<link rel="stylesheet" href="https://fonts.googleapis.com/css2?family=Questrial&display=swap">
<style>
  :root {
    --bg: #d9d9d7;
    --card-black: #141414;
    --brand-blue: #3cb8e2;
    --blue-light: #6fd3ef;
    --blue-deep: #36aedb;
    --white: #ffffff;
    --ink: #111111;
  }
  * { box-sizing: border-box; margin: 0; padding: 0; }
  html, body {
    width: 1200px; height: 1000px; overflow: hidden;
    background: var(--bg);
    font-family: "Questrial", "Century Gothic", sans-serif;
  }
  .canvas {
    position: relative; width: 1200px; height: 1000px;
    display: flex; flex-direction: column; align-items: center; justify-content: center; gap: 48px;
  }
  .card {
    position: relative; width: 700px; height: 428px; overflow: hidden;
    box-shadow: 0 6px 18px rgba(0,0,0,0.18);
  }

  /* Back of card */
  .card--back { background: var(--card-black); color: var(--white); }
  .holder { position: absolute; left: 210px; top: 52px; }
  .holder__name { font-size: 30px; letter-spacing: 0.5px; }
  .holder__role { font-size: 21px; color: var(--brand-blue); line-height: 1.25; margin-top: 4px; }
  .brand--small {
    position: absolute; right: 44px; top: 128px;
    font-size: 36px; color: var(--white); letter-spacing: -0.5px;
  }
  .contact { position: absolute; left: 110px; top: 232px; }
  .contact__row { display: flex; align-items: center; height: 40px; margin-bottom: 8px; }
  .contact__label {
    width: 150px; height: 36px; background: var(--brand-blue);
    font-size: 21px; color: var(--white); padding: 5px 10px;
  }
  .contact__value { margin-left: 22px; font-size: 20px; letter-spacing: 0.6px; white-space: nowrap; }

  /* Front of card */
  .card--front { background: linear-gradient(160deg, var(--blue-deep) 0%, var(--brand-blue) 45%, var(--blue-light) 100%); }
  .brand--large {
    position: absolute; left: 0; right: 0; top: 120px; text-align: center;
    font-size: 100px; color: var(--ink); letter-spacing: -2px;
  }
  .mobile-band {
    position: absolute; left: 0; right: 0; top: 300px; height: 74px;
    background: var(--white);
    display: flex; align-items: center; padding-left: 150px;
  }
  .mobile-band__text { font-size: 34px; color: var(--ink); letter-spacing: 1px; }
</style>
</head>
<body>
<main class="canvas">
  <section class="card card--back" aria-label="Business card back">
    <div class="holder">
      <h1 class="holder__name">Owen Presley</h1>
      <p class="holder__role">Director<br>Mobile Mortgage Broker</p>
    </div>
    <p class="brand brand--small">nests2keys</p>
    <div class="contact">
      <div class="contact__row"><span class="contact__label">Address:</span><span class="contact__value">PO BOX 2984 West Calder NSW 2175</span></div>
      <div class="contact__row"><span class="contact__label">Tel:</span><span class="contact__value">0471 286 904</span></div>
      <div class="contact__row"><span class="contact__label">email:</span><span class="contact__value">owen@brickvaleplex.com.au</span></div>
    </div>
  </section>

  <section class="card card--front" aria-label="Business card front">
    <p class="brand brand--large">nests2keys</p>
    <div class="mobile-band"><span class="mobile-band__text">M: 0471 286 904</span></div>
  </section>
</main>
</body>
</html>
```